KR Stationary Design

Logo, Business Card, Letterhead & Email Signature Design

Target Market(s)

Legal

Colors

Designer to choose colors to be used in the design.

Requirements
Must have
• Gold and Blue are the colours to use. The KR must be inside the Gold Legal Pendulum

```html
<!DOCTYPE html>
<html lang="en">
<head>
<meta charset="utf-8">
<title>KR Rantsho Incorporated – Business Card</title>
<link rel="stylesheet" href="https://fonts.googleapis.com/css2?family=Libre+Baskerville:wght@700&family=Montserrat:wght@400;500&display=swap">
<style>
  :root {
    --gold: #b38a2e;
    --gold-light: #d9b45a;
    --blue: #2a78c2;
    --ink: #3a3a3a;
    --paper: #f8f7f5;
    --night: #1c1c1c;
    --backdrop: #d6d5d1;
  }
  * { box-sizing: border-box; margin: 0; padding: 0; }
  html, body { width: 1200px; height: 906px; overflow: hidden; }
  body {
    background: var(--backdrop);
    font-family: "Montserrat", sans-serif;
    position: relative;
  }
  .card {
    position: absolute;
    left: 250px;
    width: 700px;
    height: 400px;
    border-bottom: 3px solid var(--gold-light);
    border-right: 3px solid var(--gold-light);
    box-shadow: 0 6px 18px rgba(0,0,0,0.18);
  }
  .card--front { top: 40px; background: var(--paper); }
  .card--back { top: 466px; background: var(--night); }

  .firm-name {
    font-family: "Libre Baskerville", serif;
    font-weight: 700;
    color: var(--gold);
    text-align: center;
    letter-spacing: 2px;
    line-height: 1.2;
  }
  .card--front .firm-name {
    position: absolute;
    left: 30px; top: 140px; width: 300px;
    font-size: 26px;
  }
  .card--back .firm-name {
    position: absolute;
    left: 0; right: 0; top: 150px;
    font-size: 40px;
    color: var(--gold-light);
  }

  .divider {
    position: absolute;
    left: 355px; top: 60px;
    width: 1.5px; height: 280px;
    background: var(--gold);
  }

  .contact {
    position: absolute;
    left: 385px; top: 62px;
    width: 290px;
  }
  .contact__name {
    font-family: "Libre Baskerville", serif;
    font-weight: 700;
    font-size: 24px;
    color: var(--gold);
  }
  .contact__role {
    font-size: 13px;
    color: var(--ink);
    margin-top: 4px;
  }
  .contact__address {
    font-size: 13px;
    color: var(--ink);
    line-height: 1.5;
    margin-top: 22px;
    font-style: normal;
  }
  .contact__list {
    list-style: none;
    margin-top: 18px;
  }
  .contact__item {
    display: flex;
    align-items: center;
    gap: 10px;
    font-size: 13px;
    color: var(--ink);
    line-height: 1.75;
  }
  .contact__icon { width: 14px; height: 14px; flex: none; }
</style>
</head>
<body>

<section class="card card--front" aria-label="Business card front">
  <h1 class="firm-name">KR Rantsho<br>Incorporated</h1>
  <div class="divider"></div>
  <div class="contact">
    <p class="contact__name">Kabelo Rantsho</p>
    <p class="contact__role">Director</p>
    <address class="contact__address">
      Block C Larkspur Office Park<br>
      42 Elmhurst Road North<br>
      Fernhill, 2040
    </address>
    <ul class="contact__list">
      <li class="contact__item">
        <svg class="contact__icon" viewBox="0 0 16 16" aria-hidden="true"><path fill="#b38a2e" d="M3.6 1.5l2.3 2.6-1.3 1.6c.9 2 2.6 3.7 4.6 4.6l1.6-1.3 2.6 2.3-1.5 2.2C6.7 13.3 2.7 9.3 1.5 3z"/></svg>
        011 555 0148
      </li>
      <li class="contact__item">
        <svg class="contact__icon" viewBox="0 0 16 16" aria-hidden="true"><rect x="4" y="1" width="8" height="5" fill="#b38a2e"/><rect x="1" y="6" width="14" height="7" rx="1.5" fill="#b38a2e"/><rect x="4" y="10" width="8" height="5" fill="#f8f7f5" stroke="#b38a2e"/></svg>
        086 555 0192 (Fax)
      </li>
      <li class="contact__item">
        <svg class="contact__icon" viewBox="0 0 16 16" aria-hidden="true"><rect x="1" y="3" width="14" height="10" fill="#b38a2e"/><path d="M1 3l7 6 7-6" fill="none" stroke="#f8f7f5" stroke-width="1.4"/></svg>
        kabelo@krrantsho.co.za
      </li>
    </ul>
  </div>
</section>

<section class="card card--back" aria-label="Business card back">
  <h2 class="firm-name">KR Rantsho<br>Incorporated</h2>
</section>

</body>
</html>
```